Business Card Design Project

A new design for our business cards for a small casting/talent agency, we would like to incorporate the logo and brand colors within the design, below are the information that should be on the card

(Name)
(Title)

Corvel Arta FZ-LLC
Brindle Quay Park
Building 27, Suite 418
Dubai, UAE
PO Box 871465
+97140000000
info@CorvelArta-example.com

Target Market(s)

production companies, film makers, media, entertainment industry

Industry/Entity Type

Business

Requirements
Must have
• logo, logo colors
Nice to have
• cutting edge design, sleek and modern
Should not have
• playful, funky, congested

```html
<!DOCTYPE html>
<html lang="en">
<head>
<meta charset="utf-8">
<title>Corvel Arta — Business Cards</title>
<link rel="stylesheet" href="https://fonts.googleapis.com/css2?family=Jost:wght@400;500;600&display=swap">
<style>
  :root {
    --stage: #2a2a2c;
    --card: #ffffff;
    --navy: #1b2456;
    --silver: #c3cdd8;
    --silver-deep: #9fadbd;
    --steel: #a8b6c6;
    --grey: #9b9b9b;
    --grey-dark: #8a8a8a;
  }
  * { box-sizing: border-box; margin: 0; padding: 0; }
  html, body { width: 1200px; height: 870px; overflow: hidden; }
  body {
    background: var(--stage);
    font-family: "Jost", "Futura", sans-serif;
    position: relative;
  }
  .card {
    position: absolute;
    top: 280px;
    width: 540px;
    height: 310px;
    background: var(--card);
    overflow: hidden;
  }
  .card--front { left: 40px; }
  .card--back { left: 620px; }
  .card__swoosh { position: absolute; inset: 0; width: 100%; height: 100%; }

  .brand { position: absolute; display: flex; align-items: center; gap: 12px; }
  .brand__dot { border-radius: 50%; background: var(--navy); flex: none; }
  .brand__name { color: var(--navy); font-weight: 500; letter-spacing: 0.5px; }

  .card--front .brand { left: 30px; top: 34px; }
  .card--front .brand__dot { width: 62px; height: 62px; }
  .card--front .brand__name { font-size: 26px; }

  .person { position: absolute; left: 30px; top: 120px; }
  .person__name { color: var(--navy); font-size: 22px; font-weight: 600; letter-spacing: 0.5px; }
  .person__title { color: var(--steel); font-size: 17px; font-weight: 500; margin-left: 22px; }

  .contact { position: absolute; right: 28px; top: 118px; text-align: right; }
  .contact__address {
    color: var(--grey);
    font-size: 15px;
    letter-spacing: 2.5px;
    line-height: 1.3;
    font-style: normal;
  }
  .contact__phone {
    color: var(--grey-dark);
    font-size: 24px;
    letter-spacing: 1.5px;
    margin-top: 12px;
  }
  .contact__email { color: var(--navy); font-size: 17px; font-weight: 500; }

  .card--back .brand { left: 74px; top: 56px; gap: 16px; }
  .card--back .brand__dot { width: 104px; height: 104px; }
  .card--back .brand__name { font-size: 38px; }

  .web {
    position: absolute;
    right: 10px;
    bottom: 18px;
    color: var(--steel);
    font-size: 13px;
    letter-spacing: 1px;
    writing-mode: vertical-rl;
    transform: rotate(180deg);
  }
</style>
</head>
<body>

<section class="card card--front" aria-label="Business card front">
  <svg class="card__swoosh" viewBox="0 0 540 310" aria-hidden="true">
    <path d="M0 0 H540 V46 C400 18 220 14 0 70 Z" fill="var(--silver)"/>
    <path d="M120 0 C300 6 440 20 540 60 V46 C430 14 300 4 120 0 Z" fill="var(--silver-deep)"/>
    <path d="M0 310 V238 C90 206 200 226 290 310 Z" fill="var(--silver)"/>
    <path d="M0 238 C90 206 200 226 290 310 H276 C196 236 96 218 0 248 Z" fill="var(--silver-deep)"/>
  </svg>

  <div class="brand">
    <span class="brand__dot"></span>
    <span class="brand__name">Corvel Arta</span>
  </div>

  <div class="person">
    <p class="person__name">Your Name</p>
    <p class="person__title">Title</p>
  </div>

  <div class="contact">
    <address class="contact__address">
      Brindle Quay Park<br>
      Building 27, Suite 418<br>
      Dubai, UAE, 871465
    </address>
    <p class="contact__phone">+97140000000</p>
    <p class="contact__email">info@CorvelArta-example.com</p>
  </div>
</section>

<section class="card card--back" aria-label="Business card back">
  <svg class="card__swoosh" viewBox="0 0 540 310" aria-hidden="true">
    <path d="M180 0 H540 V130 C470 64 340 18 180 0 Z" fill="var(--silver)"/>
    <path d="M180 0 C350 16 470 60 540 130 V150 C460 70 340 20 180 0 Z" fill="var(--silver-deep)"/>
    <path d="M0 310 V262 C130 222 310 232 430 310 Z" fill="var(--silver)"/>
    <path d="M0 262 C130 222 310 232 430 310 H414 C300 240 130 232 0 272 Z" fill="var(--silver-deep)"/>
  </svg>

  <div class="brand">
    <span class="brand__dot"></span>
    <span class="brand__name">Corvel Arta</span>
  </div>

  <p class="web">www.CorvelArta-example.com</p>
</section>

</body>
</html>
```